Classic and neutral book cover design

We are looking for a classic and neutral book cover design to be used as the template for a series of books to be published. We are hence looking for a template that will allow us to easily change the title name for all books in this series.
The use of very few colours (black and white is welcome) and few design elements is a big bonus. As a source of inspiration we would like to ask you to view the very simple and
If you think you have a cool idea that can add a twist to the formal classic look don't hesitate. Go for it !
Work will be done for a 30 year old Sweden based cultural non-profit called VĂ©lra (www.velrafoundation.example). We work with the publishing and supporting of post-modern art and literature addressing contemporary topics but are also involved in assisting projects of cultural preservation.
Target Market(s)
The audience is expected to have some form of interest in culture but could range from hobbyist readers to tenure track scholars
Industry/Entity Type
Non-Profit
Requirements
Must have
- General:
- Classic and neutral feel
- Preferably very simple and few shapes
- usage of few colours (black and white is welcome)
Information to be displayed on the cover is:
- Author
- Title
- type of work e.g. play/novel (optional)
- publishing house (in this case "Velra Publishing")
Nice to have
- ideas to prevent it from become boring are of course welcome
Should not have
- - too many colours

```html
<!DOCTYPE html>
<html lang="en">
<head>
<meta charset="utf-8">
<title>Series Cover — Vélra Publishing</title>
<link rel="stylesheet" href="https://fonts.googleapis.com/css2?family=Jost:wght@400&display=swap">
<style>
  :root {
    --paper: #ffffff;
    --cream: #ede5d4;
    --taupe: #b7aea2;
    --ink: #111111;
  }
  html, body {
    margin: 0;
    padding: 0;
    overflow: hidden;
    background: var(--paper);
  }
  .cover {
    position: relative;
    width: 952px;
    height: 1200px;
    overflow: hidden;
    background: var(--paper);
    font-family: "Jost", "Futura", sans-serif;
    color: var(--ink);
  }
  .cover-shapes {
    position: absolute;
    inset: 0;
    display: block;
  }
  .shape-cream { fill: var(--cream); }
  .shape-taupe { fill: var(--taupe); }
  .rule {
    fill: none;
    stroke: var(--taupe);
    stroke-width: 9;
  }
  .publisher {
    position: absolute;
    left: 26px;
    top: 52px;
    margin: 0;
    font-size: 38px;
    line-height: 1;
    letter-spacing: 1px;
    font-weight: 400;
  }
  .title-block {
    position: absolute;
    left: 260px;
    top: 95px;
    width: 692px;
    height: 363px;
  }
  .title {
    margin: 0;
    padding: 28px 0 0 56px;
    font-size: 122px;
    line-height: 126px;
    font-weight: 400;
    letter-spacing: 1px;
  }
  .work-type {
    position: absolute;
    left: 710px;
    top: 462px;
    margin: 0;
    font-size: 38px;
    font-weight: 400;
  }
  .author {
    position: absolute;
    left: 0;
    top: 1066px;
    width: 952px;
    height: 94px;
  }
  .author-name {
    margin: 0;
    padding-left: 283px;
    font-size: 42px;
    line-height: 94px;
    font-weight: 400;
    letter-spacing: 0.5px;
  }
</style>
</head>
<body>
<main class="cover">
  <svg class="cover-shapes" width="952" height="1200" viewBox="0 0 952 1200" aria-hidden="true">
    <!-- upper cream panel with its left rule -->
    <rect class="shape-cream" x="350" y="0" width="602" height="100"/>
    <line class="rule" x1="350" y1="0" x2="350" y2="100"/>
    <!-- thin frame line leading into the title block -->
    <polyline class="rule" points="212,38 212,302 264,320"/>
    <!-- large cream disc -->
    <circle class="shape-cream" cx="-135" cy="1250" r="940"/>
    <circle class="rule" cx="-135" cy="1250" r="940" stroke-width="10"/>
    <!-- outer echo arc -->
    <path class="rule" stroke-width="10" d="M 500 458 A 980 980 0 0 1 838 1200"/>
    <!-- title block and author band -->
    <rect class="shape-taupe" x="260" y="95" width="692" height="363"/>
    <rect class="shape-taupe" x="0" y="1066" width="952" height="94"/>
  </svg>

  <p class="publisher">VÉLRA</p>

  <header class="title-block">
    <h1 class="title">this is a<br>longer title</h1>
  </header>

  <p class="work-type">a play</p>

  <footer class="author">
    <p class="author-name">AUTHOR’S NAME</p>
  </footer>
</main>
</body>
</html>
```